Dental office stationary (letterhead, envelopes), business cards, presentation folders

Nothing too dental outside of the logo. I will need all stationary, presentation folders, business cards. Would prefer to stay in the colors of the logo

Gordon Plaskett, DDS
Brightvale Dental Implant Center
310-555-0187
info@brightvaledental-example.com
3875 NW Orchard Pkwy Unit B
Lakemont, OR 34917

Also need appointment date and time
And cancellation policy
I want it to say “kindly ask for
A 48hr cancellation policy to avoid incurring a cancellation fee”

Dental

Colors
0054AA
0677BA
7BADD7
CADEEF
E8F1F8

Requirements
Must have
• Name of your office, name of doctor, address, phone number
Should not have
• Too much tooth/dental. Only the tooth in logo

```html
<!DOCTYPE html>
<html lang="en">
<head>
<meta charset="utf-8">
<title>Brightvale Dental Implant Center – Business Card</title>
<link href="https://fonts.googleapis.com/css2?family=Montserrat:wght@500;600;700&display=swap" rel="stylesheet">
<style>
  :root {
    --page-bg: #e9ecef;
    --card-white: #ffffff;
    --brand-blue: #1a6fc0;
    --band-blue: #14a3db;
    --band-teal: #16b89c;
    --back-blue: #2f7fc1;
    --ink: #1d1d1f;
  }
  * { margin: 0; padding: 0; box-sizing: border-box; }
  html, body {
    width: 1200px; height: 1200px; overflow: hidden;
    background: var(--page-bg);
    font-family: "Montserrat", Arial, sans-serif;
  }
  .canvas {
    width: 1200px; height: 1200px;
    display: flex; flex-direction: column; align-items: center; justify-content: center;
    gap: 60px;
  }
  .card {
    position: relative;
    width: 900px; height: 514px;
    border-radius: 34px;
    overflow: hidden;
    box-shadow: 0 10px 30px rgba(0,0,0,0.18);
  }
  .card-front { background: var(--card-white); }
  .card-back { background: var(--back-blue); display: flex; align-items: center; justify-content: center; }

  .front-band { position: absolute; left: 0; bottom: 0; width: 900px; height: 514px; }

  .wordmark { font-family: "Montserrat", Arial, sans-serif; font-weight: 600; display: flex; align-items: center; gap: 14px; }
  .wordmark-dot { border-radius: 50%; flex: none; }
  .front-wordmark { position: absolute; top: 130px; right: 70px; color: var(--band-teal); font-size: 46px; letter-spacing: 0.5px; }
  .front-wordmark .wordmark-dot { width: 22px; height: 22px; background: var(--band-teal); }
  .back-wordmark { color: #ffffff; font-size: 72px; letter-spacing: 1px; }
  .back-wordmark .wordmark-dot { width: 32px; height: 32px; background: #ffffff; }

  .contact-block { position: absolute; left: 70px; top: 215px; }
  .doctor-name { color: var(--brand-blue); font-weight: 700; font-size: 34px; line-height: 1.1; }
  .office-name { color: var(--brand-blue); font-weight: 700; font-size: 21px; margin-top: 12px; }
  .contact-list { list-style: none; margin-top: 12px; }
  .contact-list li { display: flex; align-items: flex-start; gap: 14px; color: var(--ink); font-weight: 500; font-size: 21px; line-height: 1.3; margin-bottom: 4px; }
  .contact-icon { width: 22px; height: 22px; flex: none; margin-top: 3px; fill: var(--brand-blue); }
</style>
</head>
<body>
<main class="canvas">

  <section class="card card-front" aria-label="Business card front">
    <svg class="front-band" viewBox="0 0 900 514" aria-hidden="true">
      <polygon points="0,500 0,514 555,514 570,468" fill="var(--band-blue)"/>
      <polygon points="585,468 570,514 900,514 900,400" fill="var(--band-teal)"/>
    </svg>

    <div class="wordmark front-wordmark">
      <span class="wordmark-dot"></span>
      <span class="wordmark-name">Brightvale</span>
    </div>

    <div class="contact-block">
      <h1 class="doctor-name">Gordon Plaskett, DDS</h1>
      <p class="office-name">Brightvale Dental Implant Center</p>
      <ul class="contact-list">
        <li>
          <svg class="contact-icon" viewBox="0 0 24 24" aria-hidden="true"><path d="M6.6 10.8a15.1 15.1 0 0 0 6.6 6.6l2.2-2.2c.3-.3.7-.4 1-.2 1.1.4 2.3.6 3.6.6.6 0 1 .4 1 1V20c0 .6-.4 1-1 1A17 17 0 0 1 3 4c0-.6.4-1 1-1h3.5c.6 0 1 .4 1 1 0 1.3.2 2.5.6 3.6.1.3 0 .7-.2 1z"/></svg>
          <span>310-555-0187</span>
        </li>
        <li>
          <svg class="contact-icon" viewBox="0 0 24 24" aria-hidden="true"><path d="M2 5h20v14H2z M3.5 6.5 12 13l8.5-6.5" fill="none" stroke="var(--brand-blue)" stroke-width="2"/></svg>
          <span>info@brightvaledental-example.com</span>
        </li>
        <li>
          <svg class="contact-icon" viewBox="0 0 24 24" aria-hidden="true"><path d="M12 2a7 7 0 0 0-7 7c0 5.2 7 13 7 13s7-7.8 7-13a7 7 0 0 0-7-7zm0 9.5a2.5 2.5 0 1 1 0-5 2.5 2.5 0 0 1 0 5z"/></svg>
          <span>3875 NW Orchard Pkwy Unit B<br>Lakemont, OR 34917</span>
        </li>
      </ul>
    </div>
  </section>

  <section class="card card-back" aria-label="Business card back">
    <div class="wordmark back-wordmark">
      <span class="wordmark-dot"></span>
      <span class="wordmark-name">Brightvale</span>
    </div>
  </section>

</main>
</body>
</html>
```